Radiology Department needs a series of 3 facebook posts - similar design

We need a series of 3 posts for our facebook page, each one presenting the activity of one of 3 physicians.
The main design elements can be the same, the only thing that will change between posts will be the field of activity and name of the physician and the representative image of its activity.
If needed the design elements can be slightly different between posts for better adjustment to the representative images.
You can find as an attachment:
- Manual of institutional identity of the Hospital (Velmor Clinica)
- Our facebook cover page
- Our department video
- The representative images for each post, identified with the name of each physician
- The Institutional identity manual with the logo of "Brisa Medical School" - just for Dr Tomas Brandilo post.
So, each one of the three posts should state the name and field of activity of each physician, including somehow the corresponding representative image, and should have background innovative design elements.
Post 1:
Name of the physician: Prof. Doutor Rui Castelvo
Field of activity: Imagiologia Reumatológica e do Sistema Músculo-Esquelético
Image as an attachment
Post 2:
Name of the physician: Prof.ª Doutora Inês Barroca
Field of activity: Imagiologia Cardíaca
Image as an attachment
Post 3:
Name of the physician: Dr. Tomas Lupo
Field of activity: Tese de Doutoramento em Curso - Identificação da Lesão Cartilagínea Precoce. Com orientação do Prof. Doutor Rui Castelvo e Prof.ª Doutora Inês Sofia Carvalhal.
Image as an attachment
Just for Dr Tomas Lupo, the logo of Brisa Medical School should also be included (please check the corresponding institutional identity manual that was just added in documents).
Updates

Just for Dr Tomas Brandilo, the logo of Brisa Medical School should also be included (please check the corresponding institutional identity manual that was just added in documents).

Please note that we are just looking for 3 facebook POSTS, not facebook cover page, thanks.

Please kindly note that we are looking for facebook POST and NOT facebook cover page.

Target Market(s)

General Population

Industry/Entity Type

Health

Font styles to use
Other font styles liked:
• Check manual of institutional identity and try to approach if appropriate

Requirements
Must have
• Check project description.
Nice to have
• If the designer finds appropriate, the logo of the Hospital would be nice in all the three posts, the most simple one just stating "VelmorClinica" - please check the attached manual of institutional identity

```html
<!DOCTYPE html>
<html lang="pt">
<head>
<meta charset="utf-8">
<title>Velmor Clinica – Imagiologia</title>
<link href="https://fonts.googleapis.com/css2?family=Roboto:wght@500;700;900&family=Roboto+Condensed:wght@400;700&display=swap" rel="stylesheet">
<style>
  :root {
    --teal: #0d5c6b;
    --teal-dark: #063a44;
    --yellow: #fbb61d;
    --white: #ffffff;
    --paper: #f8f7f4;
    --black: #000000;
  }
  * { box-sizing: border-box; margin: 0; padding: 0; }
  html, body { width: 1200px; height: 313px; overflow: hidden; background: var(--white); }
  .series { position: relative; width: 1200px; height: 313px; display: flex; }
  .post { position: relative; height: 313px; overflow: hidden; }
  .post--msk { width: 413px; background: var(--white); }
  .post--cardio { width: 413px; background: var(--black); }
  .post--thesis { width: 374px; background: var(--paper); }
  .post svg.backdrop { position: absolute; left: 0; top: 0; }

  .title {
    position: absolute; font-family: "Roboto", sans-serif; font-weight: 700;
    color: var(--teal); text-transform: uppercase;
  }
  .post--msk .title { left: 182px; top: 70px; font-size: 15.6px; line-height: 17.2px; letter-spacing: 0.1px; }
  .post--cardio .title { right: 53px; top: 58px; font-size: 31px; line-height: 35px; text-align: right; font-weight: 900; letter-spacing: 0.3px; }

  .name-bar {
    position: absolute; top: 142px; height: 29px; background: var(--yellow);
    font-family: "Roboto Condensed", sans-serif; font-weight: 700; font-size: 11.6px;
    color: var(--teal); display: flex; align-items: center; justify-content: center;
    letter-spacing: 0.2px;
  }
  .post--msk .name-bar { left: 183px; width: 191px; }
  .post--cardio .name-bar { left: 183px; width: 190px; box-shadow: 2px 6px 6px rgba(0,0,0,0.15); }
  .post--thesis .name-bar { left: 183px; width: 191px; }

  .brand { position: absolute; left: 183px; top: 251px; width: 190px; }
  .brand__row { display: flex; align-items: center; gap: 5px; }
  .brand__dot { width: 37px; height: 37px; border-radius: 50%; background: var(--teal); flex: none; }
  .brand__name { font-family: "Roboto", sans-serif; font-weight: 700; font-size: 21px; color: var(--teal); letter-spacing: -0.2px; }
  .brand__tagline { font-family: "Roboto Condensed", sans-serif; font-size: 9.6px; color: var(--teal); margin-left: 41px; margin-top: 2px; }
  .post--cardio .brand__dot { background: var(--white); }
  .post--cardio .brand__name, .post--cardio .brand__tagline { color: var(--white); }

  .thesis-heading { position: absolute; left: 15px; top: 54px; right: 6px; font-family: "Roboto", sans-serif; font-weight: 700; color: var(--teal); text-transform: uppercase; }
  .thesis-heading__label { font-size: 13.2px; line-height: 13px; letter-spacing: 0.3px; }
  .thesis-heading__topic { font-size: 10.8px; line-height: 12px; letter-spacing: 0.4px; }
  .thesis-heading__advisors { font-family: "Roboto Condensed", sans-serif; font-size: 8.3px; line-height: 10px; margin-top: 5px; }

  .school-name { position: absolute; right: 12px; top: 15px; font-family: "Roboto", sans-serif; font-weight: 700; font-size: 11px; color: var(--teal); text-transform: uppercase; letter-spacing: 0.3px; }
</style>
</head>
<body>
<main class="series">

  <section class="post post--msk">
    <svg class="backdrop" width="413" height="313" viewBox="0 0 413 313">
      <defs>
        <radialGradient id="xray-tone" cx="0.4" cy="0.45" r="0.6">
          <stop offset="0" stop-color="#8a8a8a"/>
          <stop offset="0.6" stop-color="#3a3a3a"/>
          <stop offset="1" stop-color="#050505"/>
        </radialGradient>
      </defs>
      <circle cx="0" cy="156" r="161" fill="var(--yellow)"/>
      <circle cx="0" cy="156" r="140" fill="url(#xray-tone)" role="img" aria-label="Radiografia das mãos com imagem angiográfica"/>
    </svg>
    <h2 class="title">Imagiologia<br>Reumatológica<br>e do Sistema<br>Músculo-Esquelético</h2>
    <div class="name-bar">PROF. DOUTOR RUI CASTELVO</div>
    <div class="brand">
      <div class="brand__row"><span class="brand__dot"></span><span class="brand__name">VelmorClinica</span></div>
      <div class="brand__tagline">Construímos relações de confiança</div>
    </div>
  </section>

  <section class="post post--cardio">
    <svg class="backdrop" width="413" height="313" viewBox="0 0 413 313">
      <defs>
        <linearGradient id="teal-floor" x1="0" y1="0" x2="1" y2="1">
          <stop offset="0.35" stop-color="#000"/>
          <stop offset="1" stop-color="var(--teal)"/>
        </linearGradient>
        <radialGradient id="heart-tone" cx="0.5" cy="0.55" r="0.55">
          <stop offset="0" stop-color="#8a2a22"/>
          <stop offset="0.8" stop-color="#5a1712"/>
          <stop offset="1" stop-color="#3a0e0a"/>
        </radialGradient>
      </defs>
      <rect width="413" height="313" fill="url(#teal-floor)"/>
      <path d="M95,0 Q110,215 373,254 L413,254 L413,0 Z" fill="var(--white)"/>
      <rect x="167" y="38" width="206" height="9" fill="var(--yellow)"/>
      <ellipse cx="68" cy="160" rx="55" ry="58" fill="url(#heart-tone)" role="img" aria-label="Reconstrução 3D do coração com artérias coronárias"/>
    </svg>
    <h2 class="title">Imagiologia<br>Cardíaca</h2>
    <div class="name-bar">PROF.ª DOUTORA INÊS BARROCA</div>
    <div class="brand">
      <div class="brand__row"><span class="brand__dot"></span><span class="brand__name">VelmorClinica</span></div>
      <div class="brand__tagline">Construímos relações de confiança</div>
    </div>
  </section>

  <section class="post post--thesis">
    <svg class="backdrop" width="374" height="313" viewBox="0 0 374 313">
      <defs>
        <radialGradient id="mri-tone" cx="0.5" cy="0.45" r="0.55">
          <stop offset="0" stop-color="#1a3fd0"/>
          <stop offset="0.7" stop-color="#0a28b8"/>
          <stop offset="1" stop-color="#061a80"/>
        </radialGradient>
      </defs>
      <circle cx="63" cy="221" r="121" fill="var(--yellow)" role="img" aria-label="Elemento decorativo circular em amarelo"/>
      <circle cx="63" cy="221" r="62" fill="url(#mri-tone)" role="img" aria-label="Ressonância magnética do joelho com mapa de cores da cartilagem"/>
    </svg>
    <div class="school-name">Brisa Medical School</div>
    <div class="thesis-heading">
      <p class="thesis-heading__label">Tese de Doutoramento em Curso</p>
      <p class="thesis-heading__topic">Identificação da Lesão Cartilagínea Precoce.</p>
      <p class="thesis-heading__advisors">Com orientação do Prof. Doutor Rui Castelvo e Prof.ª Doutora Inês Sofia Carvalhal.</p>
    </div>
    <div class="name-bar">DR. TOMAS LUPO</div>
    <div class="brand">
      <div class="brand__row"><span class="brand__dot"></span><span class="brand__name">VelmorClinica</span></div>
      <div class="brand__tagline">Construímos relações de confiança</div>
    </div>
  </section>

</main>
</body>
</html>
```